Create Homepage Header & Search Box for Education Website

This project is relatively small and pays well.
Site: brightvalelearning.org
Project Title:
Redesign slider to be a static image/graphic and include a 3 drop down search box.
Project Summary:
We need a new homepage header for brightvalelearning.org. The logo, top navigation, and social buttons should remain unchanged. The new header needs to include a static graphic or image and a 3 drop down search box. It can also include some text that speaks to the what our site provides. For text suggestions - see below. Placement for the search box should be to the left under the logo. We will remove the slider functionality and need the design to be static.
Below the current slider images are bar graphs and a pie graph. These can remain as is - or you can make design changes. If you make design changes - please be sure the message doesn't change. Also you can submit one version of the design with this removed if you feel like it helps best accomplish our goal of conversion.
Project Objectives:
The primary objective of the deign is to maximize conversion of clicks to the search box. We need users to gravitate to the search box. Additionally the design should convey trust and academic feel.
Target Market:
High School Graduates and people in their 20s looking for college options.
Potential text:
Tagline Option: "Your #1 Resource for an Affordable Online College Education"
Tagline Option: "Find Affordable Online College Options"
Other Details: Brightvale Learning Hub will help you find a more affordable college experience. Look no further to find financial aid information, cost saving tips, and comprehensive college rankings focused on affordability and value.
Or you can also use some placeholder text and I can create the right messaging.
The Search Box:
The search box is pretty standard - you can see examples in the examples below - or in the files I attached. 3 drop downs and a "Search" button.
Examples of some previous designs attached to the project:
These designs are close - but not perfect. These will give you a good general idea for what we need.
Examples of designs at similar websites:
kwpn.org
studyharborhub.net
topmeadowcourses.com

```html
<!DOCTYPE html>
<html lang="en">
<head>
<meta charset="utf-8">
<title>Brightvale Learning Hub – Find Affordable Online College Options</title>
<link href="https://fonts.googleapis.com/css2?family=Cabin+Sketch:wght@400;700&family=Bree+Serif&family=Oswald:wght@500;600&family=Open+Sans:wght@400;600&display=swap" rel="stylesheet">
<style>
  :root{
    --orange:#f26a3b;
    --orange-dark:#d9532a;
    --navy:#1f3752;
    --navy-deep:#152638;
    --band:#161d26;
    --teal:#1f5f66;
    --green:#6fbf8e;
    --green-dark:#4f9e70;
    --board:#2f4a34;
    --frame:#b7773c;
    --text:#4a4a4a;
    --muted:#7a8a99;
    --white:#ffffff;
  }
  *{box-sizing:border-box;margin:0;padding:0}
  html,body{width:1200px;height:708px;overflow:hidden;background:var(--white)}
  body{position:relative;font-family:"Open Sans",sans-serif;color:var(--text)}

  .site-header{position:absolute;left:0;top:0;width:1200px;height:84px;background:var(--white)}
  .brand{position:absolute;left:58px;top:28px;display:flex;align-items:center;gap:10px}
  .brand-dot{width:28px;height:28px;border-radius:50%;background:var(--orange)}
  .brand-name{font-weight:600;font-size:15px;color:var(--orange)}
  .main-nav{position:absolute;left:293px;top:33px;display:flex;gap:38px}
  .main-nav a{font-size:17px;letter-spacing:1px;color:#333;text-decoration:none;padding-bottom:6px}
  .main-nav a.is-active{color:var(--orange);border-bottom:2px solid var(--orange)}
  .social{position:absolute;left:1015px;top:33px;display:flex;gap:16px}
  .social span{width:26px;height:26px;border-radius:4px;background:var(--navy)}

  .hero{position:absolute;left:0;top:84px;width:1200px;height:363px;overflow:hidden;
    background:radial-gradient(ellipse at 55% 40%,#274463 0%,var(--navy) 55%,var(--navy-deep) 100%)}
  .hero-title{position:absolute;left:318px;top:44px;width:612px;text-align:center;z-index:2;white-space:nowrap;
    font-family:"Cabin Sketch",sans-serif;font-weight:700;font-size:31px;color:#eef2f5}

  .search-box{position:absolute;left:19px;top:53px;width:255px;height:291px;background:var(--green);
    border:1px solid var(--green-dark)}
  .search-ribbon{position:absolute;left:20px;top:16px;width:256px;height:42px;background:var(--orange);
    text-align:center;color:var(--white);font-family:"Bree Serif",serif;padding-left:30px}
  .search-ribbon strong{display:block;font-size:20px;font-weight:400;line-height:24px;margin-top:2px}
  .search-ribbon small{display:block;font-size:11px;line-height:12px}
  .get-info{position:absolute;left:9px;top:8px;width:54px;height:54px;border-radius:50%;background:var(--orange-dark);
    border:2px solid var(--green);color:var(--white);font-family:"Bree Serif",serif;font-size:11px;
    line-height:12px;text-align:center;padding-top:13px}
  .field{position:absolute;left:12px;display:flex;align-items:center;gap:8px}
  .step{width:26px;height:26px;border-radius:50%;background:var(--orange);color:var(--white);
    font-family:"Bree Serif",serif;font-size:13px;text-align:center;line-height:26px}
  .select{width:194px;height:34px;background:#eef1f5;border:1px solid #c9d2da;
    font-family:"Bree Serif",serif;font-size:11.5px;color:#5b6670;padding:0 10px;
    display:flex;align-items:center;justify-content:space-between}
  .select::after{content:"⬍";font-size:11px;color:#777}
  .search-btn{position:absolute;left:70px;top:235px;width:142px;height:44px;padding:3px;
    background:var(--green-dark);border:1px solid #3f8a5e}
  .search-btn span{display:block;height:100%;background:var(--orange);color:var(--white);
    font-family:"Bree Serif",serif;font-size:16px;text-align:center;line-height:36px}

  .chalkboard{position:absolute;left:384px;top:117px;width:462px;height:260px;transform:rotate(-2deg);
    background:radial-gradient(ellipse at 50% 40%,#3a5a40 0%,var(--board) 70%,#22382a 100%);
    border:12px solid var(--frame);box-shadow:0 6px 14px rgba(0,0,0,.45)}
  .chalk-text{position:absolute;left:30px;top:42px;width:382px;text-align:center;
    font-family:"Cabin Sketch",sans-serif;font-weight:700;font-size:17px;line-height:20px;color:#f1f4ee;transform:rotate(2deg)}
  .board-actions{position:absolute;left:90px;top:190px;display:flex;gap:24px;transform:rotate(2deg)}
  .board-actions span{background:#e8a370;border:1px solid #a96335;color:#2c2c2c;
    font-family:"Bree Serif",serif;font-size:12.5px;padding:5px 10px}

  .hero-photo{position:absolute;left:892px;top:40px;width:226px;height:323px;z-index:1;
    border-radius:50% 50% 0 0 / 34% 34% 0 0;
    background:linear-gradient(180deg,#3a2f2c 0%,#d9b8a3 35%,#f2f3f5 60%,#e2e6ea 100%)}

  .stats{position:absolute;left:0;top:447px;width:1200px;height:140px;background:var(--band)}
  .bar{position:absolute;left:63px;width:187px;height:41px;border:1px solid #24313c}
  .bar-fill{height:100%;background:var(--teal);color:var(--white);font-family:"Oswald",sans-serif;
    font-size:27px;line-height:39px;padding-left:22px}
  .stat-label{position:absolute;left:276px;font-family:"Oswald",sans-serif;font-weight:600;
    font-size:18px;color:var(--orange)}
  .pie{position:absolute;left:503px;top:18px}
  .pie-value{position:absolute;left:503px;top:57px;width:96px;text-align:center;font-family:"Oswald",sans-serif;
    font-size:24px;color:var(--white)}
  .pie-label{position:absolute;left:615px;top:63px;font-family:"Oswald",sans-serif;font-weight:600;
    font-size:18px;line-height:24px;color:var(--orange)}
  .stats-copy{position:absolute;left:782px;top:30px;width:404px;text-align:center}
  .stats-copy h2{font-weight:400;font-size:17px;line-height:22px;color:var(--orange);margin-bottom:6px;white-space:nowrap}
  .stats-copy p{font-size:15.5px;line-height:23px;color:var(--white)}

  .features{position:absolute;left:0;top:587px;width:1200px;height:121px}
  .feature{position:absolute;top:0}
  .feature-icon{position:absolute;left:0;top:45px;width:92px;height:92px;border-radius:50%;background:var(--orange)}
  .feature h3{position:absolute;left:104px;top:50px;width:250px;font-weight:400;font-size:18px;line-height:24px;color:#444}
  .feature p{position:absolute;left:104px;width:240px;font-size:14px;line-height:22px;color:var(--muted)}
</style>
</head>
<body>
  <header class="site-header">
    <div class="brand"><span class="brand-dot"></span><span class="brand-name">Brightvale Learning Hub</span></div>
    <nav class="main-nav">
      <a class="is-active" href="#">Home</a>
      <a href="#">Financial Aid</a>
      <a href="#">Cost Savings</a>
      <a href="#">Colleges</a>
      <a href="#">Awards</a>
      <a href="#">Blog</a>
    </nav>
    <div class="social"><span aria-label="Social link"></span><span aria-label="Social link"></span><span aria-label="Social link"></span></div>
  </header>

  <section class="hero">
    <h1 class="hero-title">find affordable online college options</h1>

    <form class="search-box">
      <div class="search-ribbon"><strong>Search Here</strong><small>Request More Information</small></div>
      <div class="get-info">GET<br>INFO</div>
      <div class="field" style="top:82px"><span class="step">1</span><div class="select">Choose a Degree Level</div></div>
      <div class="field" style="top:133px"><span class="step">2</span><div class="select">Choose a Category</div></div>
      <div class="field" style="top:184px"><span class="step">3</span><div class="select">Choose a Subject</div></div>
      <div class="search-btn"><span>Search Now</span></div>
    </form>

    <div class="chalkboard">
      <p class="chalk-text">brightvale learning hub will help you find a more affordable college experience. look no further to find financial aid information, cost saving tips, and comprehensive college rankings focused on affordability and value</p>
      <div class="board-actions"><span>Compare Colleges</span><span>Request Information</span></div>
    </div>

    <div class="hero-photo" role="img" aria-label="Photo of a smiling teacher in a white coat holding chalk beside the chalkboard"></div>
  </section>

  <section class="stats">
    <div class="bar" style="top:20px"><div class="bar-fill" style="width:105px">$12,500</div></div>
    <div class="stat-label" style="top:29px">AVG STUDENT DEBT IN 1996</div>
    <div class="bar" style="top:76px"><div class="bar-fill" style="width:155px">$26,600</div></div>
    <div class="stat-label" style="top:85px">AVG STUDENT DEBT IN 2011</div>

    <svg class="pie" width="96" height="96" viewBox="0 0 96 96" aria-hidden="true">
      <circle cx="48" cy="48" r="48" fill="#1a2a36"/>
      <path d="M48 48 L48 0 A48 48 0 1 1 6.4 71.9 Z" fill="#1f5f66"/>
    </svg>
    <div class="pie-value">66%</div>
    <div class="pie-label">PCT OF STUDENTS<br>WITH LOANS</div>

    <div class="stats-copy">
      <h2>College Costs Rising &amp; Student Debt Ballooning</h2>
      <p>Brightvale Learning Hub helps students find affordable college options and provides information about financial aid and college rankings.</p>
    </div>
  </section>

  <section class="features">
    <div class="feature" style="left:85px">
      <div class="feature-icon"><svg width="92" height="92" viewBox="0 0 92 92" aria-hidden="true"><text x="46" y="62" text-anchor="middle" font-family="Open Sans,sans-serif" font-weight="600" font-size="46" fill="#fff">$</text></svg></div>
      <h3>Financial Aid</h3>
      <p style="top:85px">The nuts of bolts of financial aid – what's available and how to apply.</p>
    </div>
    <div class="feature" style="left:451px">
      <div class="feature-icon"><svg width="92" height="92" viewBox="0 0 92 92" aria-hidden="true"><g fill="#fff"><rect x="24" y="52" width="8" height="18"/><rect x="36" y="44" width="8" height="26"/><rect x="48" y="38" width="8" height="32"/><rect x="60" y="30" width="8" height="40"/></g><polyline points="22,44 36,34 48,30 66,18" fill="none" stroke="#fff" stroke-width="3"/></svg></div>
      <h3>Rising College Costs: Who is Helping?</h3>
      <p style="top:110px">Who's helping and what does that mean.</p>
    </div>
    <div class="feature" style="left:816px">
      <div class="feature-icon"><svg width="92" height="92" viewBox="0 0 92 92" aria-hidden="true"><ellipse cx="46" cy="50" rx="24" ry="18" fill="#fff"/><rect x="36" y="64" width="6" height="8" fill="#fff"/><rect x="52" y="64" width="6" height="8" fill="#fff"/><text x="46" y="57" text-anchor="middle" font-family="Open Sans,sans-serif" font-weight="600" font-size="18" fill="#f26a3b">$</text></svg></div>
      <h3>Affordability Tips</h3>
      <p style="top:85px">Check out our tips for how you can make college more affordable.</p>
    </div>
  </section>
</body>
</html>
```